New cake shop needs a gorgeous website!

I need an easy to navigate and update (from my Mac - in layman's terms!) website for my new business - Crumb & Fern. This is a dietary friendly cake shop in Harbourvale, Auckland, New Zealand. We will be having Tarawhiti coffee (organic, fair-trade) Lumen Fizz range and specialty teas. Eat in, takeaway and delivery.
I will require you to upload and write if necessary, onto a program such as Pagecraft or similar.
I need a homepage, gallery page, price and ordering page (although the orders will be done via email/phone, no payments will be taken directly from the website) about us page, products and services page(this could incorporate the gallery maybe) a classes info page and a contact page.
My branding is very modern and clean. No vintage or french industrial is to be seen! We are sleek, with lots of white, black, charcoal grey and hot pink.
I will have photos to use in about 10 days, but I will upload some temporary images to start you off....
We also have a focus on 'a little bit good for you' and aim to make cakes that everyone can eat, whether they be gluten, dairy or egg intolerant or trying to lower the sugar in their diet.
A great design will be modern, exciting and convey a feel of luxury.
Please check out my pinterest page http://www.pinboardly.example/wrenbolt/coffee-cards-flyers-and-websites/
and feel free to use images from my instagram - fernbakenz.
Thanks!

```html
<!DOCTYPE html>
<html lang="en">
<head>
<meta charset="utf-8">
<title>Crumb &amp; Fern — Dietary Friendly Cake Shop</title>
<link href="https://fonts.googleapis.com/css2?family=Montserrat:wght@700&family=Raleway:wght@400;500;600;700&display=swap" rel="stylesheet">
<style>
  :root {
    --pink: #e0439a;
    --white: #ffffff;
    --ink: #1f1f1f;
    --text: #4a4a4a;
    --grey-soft: #ececec;
    --grey-line: #cfcfcf;
    --grey-icon: #b9b9b9;
    --black-bar: #141414;
  }
  * { box-sizing: border-box; margin: 0; padding: 0; }
  html, body { width: 950px; height: 1200px; overflow: hidden; background: var(--white); }
  body { font-family: "Raleway", Arial, sans-serif; color: var(--text); position: relative; }

  .container { width: 676px; margin: 0 auto; position: relative; }

  /* Hero */
  .hero { position: relative; height: 524px; border-bottom: 3px solid var(--pink); overflow: hidden; }
  .hero-photo {
    position: absolute; inset: 0;
    background:
      radial-gradient(ellipse 30% 22% at 55% 18%, rgba(236,196,40,.85), transparent 70%),
      radial-gradient(ellipse 28% 30% at 78% 30%, rgba(196,30,70,.8), transparent 70%),
      radial-gradient(ellipse 45% 30% at 30% 45%, rgba(226,200,220,.85), transparent 70%),
      linear-gradient(160deg, #7a4a2e 0%, #b07a6a 35%, #c46a86 55%, #6a3a22 80%, #3a2214 100%);
  }
  .hero-shade { position: absolute; inset: 0; background: rgba(40,10,20,.18); }

  .site-nav { position: absolute; top: 0; left: 0; right: 0; height: 50px; }
  .site-nav .container { display: flex; align-items: center; height: 50px; }
  .brand-mark { font-family: "Montserrat", Arial, sans-serif; font-weight: 700; font-size: 14px; color: var(--pink); letter-spacing: .3px; }
  .nav-links { margin-left: auto; display: flex; gap: 23px; list-style: none; align-items: center; }
  .nav-links li { font-size: 10px; font-weight: 500; color: var(--white); text-transform: uppercase; position: relative; }
  .nav-links li.is-active { color: var(--pink); }
  .nav-links li.is-active::before { content: ""; position: absolute; top: -18px; left: 0; right: 0; height: 2px; background: var(--white); }

  .hero-content { position: absolute; top: 210px; left: 0; right: 0; text-align: center; color: var(--white); }
  .hero-title { font-family: "Montserrat", Arial, sans-serif; font-weight: 700; font-size: 44px; letter-spacing: 1px; line-height: 1; }
  .hero-rule { width: 294px; height: 1px; background: rgba(255,255,255,.8); margin: 22px auto 10px; }
  .hero-tagline { font-size: 11px; font-weight: 600; text-transform: uppercase; width: 270px; margin: 0 auto; line-height: 1.25; }

  .pill { display: inline-flex; align-items: center; justify-content: center; gap: 8px; width: 139px; height: 25px; border-radius: 13px; font-size: 11px; text-transform: uppercase; }
  .pill-light { background: var(--white); color: var(--pink); }
  .pill-grey { background: var(--grey-soft); color: #7a7a7a; }
  .hero-content .pill { margin-top: 27px; }

  .hero-arrow { position: absolute; top: 240px; }
  .hero-arrow.prev { left: 56px; }
  .hero-arrow.next { right: 56px; }

  /* Welcome */
  .welcome { height: 232px; text-align: center; padding-top: 38px; }
  .section-title { font-size: 28px; font-weight: 500; color: var(--pink); letter-spacing: .5px; }
  .welcome p { font-size: 10px; line-height: 15px; margin-top: 10px; }
  .welcome p + p { margin-top: 0; }
  .welcome .pill { margin-top: 26px; }

  /* Recipes band */
  .recipes { position: relative; height: 257px; overflow: hidden; }
  .recipes-photo {
    position: absolute; inset: 0;
    background:
      radial-gradient(ellipse 22% 40% at 20% 10%, rgba(240,90,170,.9), transparent 70%),
      radial-gradient(ellipse 22% 40% at 62% 95%, rgba(240,80,165,.9), transparent 70%),
      radial-gradient(ellipse 18% 35% at 92% 40%, rgba(230,70,150,.85), transparent 70%),
      linear-gradient(120deg, #c21d7c 0%, #8a1e6a 45%, #6a1a55 70%, #b42679 100%);
  }
  .recipes .container { display: flex; align-items: center; height: 100%; }
  .recipes-title { width: 260px; text-align: center; color: var(--white); font-size: 42px; font-weight: 500; line-height: 58px; }
  .recipes-copy { margin-left: 40px; width: 342px; text-align: center; color: var(--white); }
  .recipes-copy p { font-size: 10px; line-height: 12px; }
  .recipes-copy .pill { margin-top: 18px; }

  /* Footer info */
  .info { height: 143px; padding-top: 33px; }
  .info .container { display: flex; gap: 17px; }
  .info-col { width: 210px; }
  .info-heading { font-size: 11px; font-weight: 700; color: var(--pink); text-transform: uppercase; padding-bottom: 6px; border-bottom: 1px solid var(--grey-line); }
  .hours { margin-top: 10px; font-size: 10px; color: var(--ink); }
  .hours-row { display: flex; justify-content: space-between; line-height: 17px; }
  .hours-row strong { font-weight: 700; }
  .address { margin-top: 10px; font-size: 10px; line-height: 12px; color: var(--ink); }
  .address strong { display: block; font-weight: 700; }
  .social { margin-top: 11px; display: flex; gap: 17px; list-style: none; }
  .social li { width: 22px; height: 22px; border-radius: 50%; background: var(--grey-icon); }

  /* Bottom bar */
  .bottom-bar { background: var(--black-bar); height: 45px; }
  .bottom-bar .container { display: flex; align-items: center; height: 45px; }
  .copyright { font-size: 10px; color: var(--pink); }
  .bottom-bar .brand-mark { margin-left: auto; font-size: 12px; }
</style>
</head>
<body>

<header class="hero">
  <div class="hero-photo" role="img" aria-label="Close-up photograph of an iced loaf cake topped with yellow flowers and crushed raspberries"></div>
  <div class="hero-shade"></div>

  <nav class="site-nav">
    <div class="container">
      <span class="brand-mark">CRUMB &amp; FERN</span>
      <ul class="nav-links">
        <li class="is-active">Home</li>
        <li>Gallery</li>
        <li>Prices</li>
        <li>Ordering</li>
        <li>About us</li>
        <li>Products&amp;Services</li>
        <li>Contact</li>
        <li aria-label="Search">
          <svg width="11" height="11" viewBox="0 0 11 11"><circle cx="4.5" cy="4.5" r="3.6" fill="none" stroke="#fff" stroke-width="1.2"/><line x1="7.2" y1="7.2" x2="10.3" y2="10.3" stroke="#fff" stroke-width="1.2"/></svg>
        </li>
      </ul>
    </div>
  </nav>

  <div class="hero-content">
    <h1 class="hero-title">CRUMB &amp; FERN</h1>
    <div class="hero-rule"></div>
    <p class="hero-tagline">Welcome to dietary friendly cake shop in Harbourvale</p>
    <span class="pill pill-light">Order now
      <svg width="5" height="7" viewBox="0 0 5 7"><polygon points="0,0 5,3.5 0,7" fill="#e0439a"/></svg>
    </span>
  </div>

  <svg class="hero-arrow prev" width="22" height="56" viewBox="0 0 22 56" aria-label="Previous slide"><polyline points="20,1 2,28 20,55" fill="none" stroke="rgba(255,255,255,.35)" stroke-width="1.5"/></svg>
  <svg class="hero-arrow next" width="22" height="56" viewBox="0 0 22 56" aria-label="Next slide"><polyline points="2,1 20,28 2,55" fill="none" stroke="#fff" stroke-width="1.5"/></svg>
</header>

<section class="welcome">
  <div class="container">
    <h2 class="section-title">WELCOME</h2>
    <p>Lorem ipsum dolor sit amet, consectetuer adipiscing elit, sed diam nonummy nibh euismod tincidunt ut laoreet dolore magna aliquam erat volutpat. Ut wisi enim ad minim veniam, quis nostrud exerci tation ullamcorper suscipit lobortis nisl ut aliquip ex ea commodo consequat.</p>
    <p>Duis autem vel eum iriure dolor in hendrerit in vulputate velit esse molestie consequat, vel illum dolore eu feugiat nulla facilisis at vero eros et accumsan et iusto odio dignissim qui blandit praesent luptatum zzril delenit augue duis dolore te feugait nulla facilisi.</p>
    <span class="pill pill-grey">About us</span>
  </div>
</section>

<section class="recipes">
  <div class="recipes-photo" role="img" aria-label="Photograph of pink meringue kisses on a dark purple surface"></div>
  <div class="container">
    <h2 class="recipes-title">DELICIOUS RECIPES</h2>
    <div class="recipes-copy">
      <p>Duis autem vel eum iriure dolor in hendrerit in vulputate velit esse molestie consequat, vel illum dolore eu feugiat nulla facilisis at vero eros et accumsan et iusto odio dignissim qui blandit praesent luptatum zzril delenit augue duis dolore te feugait nulla facilisi.</p>
      <span class="pill pill-light">Gallery
        <svg width="5" height="7" viewBox="0 0 5 7"><polygon points="0,0 5,3.5 0,7" fill="#e0439a"/></svg>
      </span>
    </div>
  </div>
</section>

<section class="info">
  <div class="container">
    <div class="info-col">
      <h3 class="info-heading">Hours</h3>
      <div class="hours">
        <div class="hours-row"><span>MONDAY - THURSDAY</span><strong>8:00pm - 10:00pm</strong></div>
        <div class="hours-row"><span>FRIDAY - SATURDAY</span><strong>8:00pm - 12:00am</strong></div>
      </div>
    </div>
    <div class="info-col">
      <h3 class="info-heading">Location</h3>
      <p class="address"><strong>CRUMB&amp;FERN.</strong>88 Kereru Lane, Harbourvale, Auckland,<br>New Zealand.</p>
    </div>
    <div class="info-col">
      <h3 class="info-heading">Social media</h3>
      <ul class="social">
        <li aria-label="Social link 1"></li>
        <li aria-label="Social link 2"></li>
        <li aria-label="Social link 3"></li>
        <li aria-label="Social link 4"></li>
        <li aria-label="Social link 5"></li>
      </ul>
    </div>
  </div>
</section>

<footer class="bottom-bar">
  <div class="container">
    <p class="copyright">Copyright © 2014. CRUMB&amp;FERN. All Rights Reserved.</p>
    <span class="brand-mark">CRUMB &amp; FERN</span>
  </div>
</footer>

</body>
</html>
```